Holiday Light Door Hanger

I need a new doorhanger design for our Holiday Light Service. I have attached our last one (which we DO like), but need to have a two-sided design. I also will attach photos that can be used as well as a FAQ about the service.

```html
<!DOCTYPE html>
<html lang="en">
<head>
<meta charset="utf-8">
<title>Holiday Light Door Hanger</title>
<link rel="stylesheet" href="https://fonts.googleapis.com/css2?family=Playfair+Display:wght@500&family=Montserrat:wght@400;500;700&family=Dancing+Script:wght@500&family=Sacramento&display=swap">
<style>
  :root {
    --backdrop: #e9e9e9;
    --navy: #2b2a57;
    --navy-deep: #24234a;
    --dusk: #5b4a7a;
    --amber: #e9a65a;
    --gold: #c49a57;
    --gold-band: #bf9a55;
    --cream: #f4f0e7;
    --ink: #1f1d2b;
    --text-light: #f5eede;
    --line: #c9a877;
    --bullet: #c99a62;
  }
  * { box-sizing: border-box; margin: 0; padding: 0; }
  html, body { width: 1200px; height: 899px; overflow: hidden; }
  body {
    background: var(--backdrop);
    font-family: "Montserrat", sans-serif;
    position: relative;
  }
  .hanger {
    position: absolute;
    top: 50px;
    width: 400px;
    height: 800px;
    overflow: hidden;
    box-shadow: 0 4px 14px rgba(0,0,0,0.12);
  }
  .hanger-front { left: 190px; background: var(--gold-band); }
  .hanger-back { left: 610px; background: var(--cream); }
  .hang-hole {
    position: absolute;
    top: 58px;
    left: 50%;
    width: 90px;
    height: 90px;
    margin-left: -45px;
    border-radius: 50%;
    background: var(--backdrop);
    z-index: 3;
  }

  /* Front */
  .night-scene {
    position: absolute;
    inset: 0 0 auto 0;
    height: 625px;
    background: linear-gradient(180deg, var(--navy-deep) 0%, var(--navy) 45%, var(--dusk) 70%, var(--amber) 100%);
  }
  .building-art {
    position: absolute;
    left: 30px;
    right: 30px;
    top: 400px;
    height: 225px;
    background: linear-gradient(180deg, #3a3560 0%, #2c2a4e 60%, #3d3a5e 100%);
    border-top: 3px solid #e0526a;
    opacity: 0.85;
  }
  .front-title {
    position: absolute;
    top: 160px;
    left: 0;
    right: 0;
    text-align: center;
    font-family: "Playfair Display", serif;
    font-weight: 500;
    font-size: 43px;
    line-height: 1.1;
    color: var(--text-light);
    letter-spacing: 0.5px;
  }
  .front-offer {
    position: absolute;
    top: 625px;
    left: 0;
    right: 0;
    bottom: 0;
    text-align: center;
    padding-top: 24px;
    color: var(--ink);
  }
  .front-offer h2 {
    font-weight: 700;
    font-size: 20px;
    line-height: 1.2;
    letter-spacing: 0.3px;
  }
  .front-offer p {
    margin: 22px auto 0;
    width: 310px;
    font-size: 13.5px;
    line-height: 1.4;
  }

  /* Back */
  .back-title {
    position: absolute;
    top: 150px;
    left: 0;
    right: 0;
    text-align: center;
    font-family: "Dancing Script", cursive;
    font-size: 30px;
    color: var(--gold);
  }
  .back-intro {
    position: absolute;
    top: 200px;
    left: 30px;
    right: 30px;
    text-align: center;
    font-size: 13.5px;
    line-height: 1.35;
    color: var(--ink);
  }
  .feature-grid {
    position: absolute;
    top: 262px;
    left: 0;
    right: 0;
    height: 320px;
  }
  .grid-line-v { position: absolute; left: 200px; top: 0; bottom: 10px; width: 1.5px; background: var(--line); }
  .grid-line-h { position: absolute; left: 10px; right: 0; top: 228px; height: 1.5px; background: var(--line); }
  .feature { position: absolute; width: 180px; }
  .feature-icon { display: block; margin: 0 auto 14px; width: 58px; height: 58px; }
  .feature ul { list-style: none; font-size: 8.5px; line-height: 1.4; color: var(--ink); }
  .feature li { position: relative; padding-left: 14px; }
  .feature li::before {
    content: ""; position: absolute; left: 0; top: 3px;
    width: 6px; height: 6px; border-radius: 50%; background: var(--bullet);
  }
  .f-protect { left: 20px; top: 8px; }
  .f-timing { left: 215px; top: 18px; }
  .f-safety { left: 18px; top: 125px; }
  .f-design { left: 215px; top: 135px; }
  .f-safety ul, .f-design ul { margin-top: 0; }
  .f-low { position: absolute; width: 180px; }
  .f-low.left { left: 14px; top: 248px; }
  .f-low.right { left: 215px; top: 248px; }

  .tree-photo {
    position: absolute;
    left: 25px;
    right: 40px;
    top: 595px;
    height: 168px;
    background: radial-gradient(ellipse at 50% 55%, #6a1a1c 0%, #2a1213 45%, #151a14 100%);
  }
  .photo-caption {
    position: absolute;
    top: 762px;
    left: 0;
    right: 15px;
    text-align: center;
    font-family: "Sacramento", cursive;
    font-size: 19px;
    color: #3a3a3a;
  }
</style>
</head>
<body>

<section class="hanger hanger-front">
  <div class="night-scene" role="img" aria-label="Night sky with glowing string lights and bokeh over a lit-up building"></div>
  <div class="building-art" role="img" aria-label="Illustration of a multi-storey building outlined with red holiday lights"></div>
  <div class="hang-hole"></div>
  <h1 class="front-title">HOLIDAY<br>LIGHT<br>INSTALATION<br>&amp; TAKEDOWN<br>SERVICES</h1>
  <div class="front-offer">
    <h2>BOOK NOW<br>BEFORE SLOTS FILL!</h2>
    <p>Tempor nostrud culpa pariatur ipsum irure sint esse aliquip incididunt. Officia duis pariatur aliqua incididunt</p>
  </div>
</section>

<section class="hanger hanger-back">
  <div class="hang-hole"></div>
  <h2 class="back-title">Holiday Light</h2>
  <p class="back-intro">Tempor nostrud culpa pariatur ipsum irure sint esse aliquip incididunt. Officia duis pariatur aliqua incididunt</p>

  <div class="feature-grid">
    <div class="grid-line-v"></div>
    <div class="grid-line-h"></div>

    <div class="feature f-protect">
      <svg class="feature-icon" viewBox="0 0 60 60" fill="none" stroke="#222" stroke-width="2">
        <path d="M30 5 L52 12 C52 32 44 46 30 55 C16 46 8 32 8 12 Z"/>
        <path d="M30 11 L46 16 C46 31 40 42 30 49 C20 42 14 31 14 16 Z"/>
      </svg>
      <ul>
        <li>Elit pariatur ad esse est anim excepteur consequat reprehenderit. Aute minim cupidatat ex aliqua dolore nulla.</li>
      </ul>
    </div>

    <div class="feature f-timing">
      <svg class="feature-icon" viewBox="0 0 60 60" fill="none" stroke="#222" stroke-width="2">
        <circle cx="30" cy="31" r="18"/>
        <path d="M30 19 V31 L38 35"/>
        <path d="M10 12 L18 18 M50 12 L42 18 M14 52 L20 46 M46 52 L40 46"/>
      </svg>
      <ul>
        <li>Elit pariatur ad esse est anim excepteur consequat reprehenderit. Aute minim cupidatat ex aliqua dolore nulla.</li>
      </ul>
    </div>

    <div class="feature f-safety">
      <svg class="feature-icon" viewBox="0 0 60 60" fill="none" stroke="#222" stroke-width="2.5">
        <path d="M24 4 L12 58 M40 4 L30 58"/>
        <path d="M22 13 H38 M20 22 H36 M18 31 H34 M16 40 H33 M14 49 H31"/>
      </svg>
    </div>

    <div class="feature f-design">
      <svg class="feature-icon" viewBox="0 0 60 60" fill="none" stroke="#222" stroke-width="2">
        <path d="M22 38 C14 32 16 16 30 16 C44 16 46 32 38 38 V44 H22 Z"/>
        <path d="M23 48 H37 M25 52 H35"/>
        <path d="M30 4 V10 M10 24 H4 M56 24 H50 M14 10 L18 14 M46 10 L42 14"/>
      </svg>
    </div>

    <div class="f-low left feature">
      <ul>
        <li>Elit pariatur ad esse est anim excepteur consequat reprehenderit.</li>
        <li>Aute minim cupidatat ex aliqua dolore nulla.</li>
      </ul>
    </div>
    <div class="f-low right feature">
      <ul>
        <li>Elit pariatur ad esse est anim excepteur consequat reprehenderit.</li>
        <li>Aute minim cupidatat ex aliqua dolore nulla.</li>
      </ul>
    </div>
  </div>

  <div class="tree-photo" role="img" aria-label="Photo of red and green light-string trees glowing at night"></div>
  <p class="photo-caption">Occaecat velit sunt anim adipisicing.</p>
</section>

</body>
</html>
```